Executive Summary

Create a one page executive summary of a venture fund - with the information here:
https://files.brindlepath.net/doc/7qR2mXvT9kLp4sWn8yZcB3fHj6dKa5eU/view?share=open

```html
<!DOCTYPE html>
<html lang="en">
<head>
<meta charset="utf-8">
<title>Fund Executive Summary</title>
<link href="https://fonts.googleapis.com/css2?family=Poppins:wght@500;600;700&family=Roboto:wght@400;500;700&display=swap" rel="stylesheet">
<style>
:root{
  --navy:#1d1d55;
  --navy-deep:#191a4d;
  --orange:#f7931e;
  --ink:#1a1a1a;
  --muted:#5a5a5a;
  --white:#ffffff;
}
*{margin:0;padding:0;box-sizing:border-box}
html,body{width:927px;height:1200px;overflow:hidden;background:var(--white)}
.page{position:relative;width:927px;height:1200px;overflow:hidden;font-family:'Roboto',sans-serif;color:var(--ink)}
.hero-art{position:absolute;left:0;top:0}
.section-title{position:absolute;font-family:'Poppins',sans-serif;font-weight:700;color:var(--navy);letter-spacing:-0.3px;line-height:1}
.rule{position:absolute;height:4px;background:var(--orange)}
.snapshot-title{left:57px;top:39px;font-size:31px}
.snapshot{position:absolute;left:57px;top:99px;width:400px;font-size:14px}
.snap-row{position:relative;height:25.5px;line-height:25.5px}
.snap-row.tall{height:51px}
.snap-label{position:absolute;left:0;white-space:nowrap;font-family:'Roboto',sans-serif;font-weight:500;font-size:17.5px;color:var(--navy)}
.snap-colon{position:absolute;left:112px;font-weight:700;color:var(--navy)}
.snap-value{position:absolute;left:138px;width:260px;font-size:14px;line-height:25.5px;color:#222}
.thesis-band{position:absolute;left:0;top:420px;width:927px;height:240px;background:var(--navy-deep);border-radius:0 180px 180px 0}
.thesis-title{left:57px;top:453px;font-size:32px;color:var(--white)}
.thesis-text{position:absolute;left:59px;top:509px;width:340px;font-family:'Poppins',sans-serif;font-weight:500;font-size:14.6px;line-height:21.8px;color:var(--white)}
.impact{position:absolute;left:61px;top:606px;font-family:'Poppins',sans-serif;font-weight:500;font-size:14.6px;color:var(--white)}
.focus-list{position:absolute;left:455px;top:456px;list-style:none}
.focus-list li{display:flex;align-items:center;height:29px;font-family:'Poppins',sans-serif;font-weight:500;font-size:15px;color:var(--white);white-space:nowrap}
.focus-list svg{width:13px;height:13px;margin-right:18px;flex:none}
.block-title{position:absolute;font-family:'Poppins',sans-serif;font-weight:700;font-size:24.5px;color:#111;line-height:1;white-space:nowrap}
.item{position:absolute;left:55px}
.item-head{display:flex;align-items:center;font-family:'Roboto',sans-serif;font-weight:500;font-size:18px;color:#111;height:22px;white-space:nowrap}
.item-head svg{width:15px;height:15px;margin-right:7px;flex:none}
.item-desc{margin-left:23px;margin-top:3px;font-size:12.6px;line-height:18px;color:var(--muted);white-space:nowrap}
.team{position:absolute;left:478px;top:678px;width:415px;height:429px;background:var(--orange);border-radius:14px}
.team-title{position:absolute;left:21px;top:23px;font-family:'Poppins',sans-serif;font-weight:700;font-size:26px;color:var(--white);line-height:1}
.team-rule{position:absolute;left:21px;top:62px;width:202px;height:4px;background:var(--white)}
.member{position:absolute;left:24px;right:12px;color:var(--white)}
.member-name{font-family:'Roboto',sans-serif;font-weight:700;font-size:18px;line-height:22px;white-space:nowrap}
.member-role{font-size:12.7px;line-height:18px;margin-top:2px;white-space:nowrap}
.footer{position:absolute;left:0;top:1145px;width:927px;height:55px;background:var(--navy-deep);color:var(--white)}
.footer-row{position:absolute;left:150px;top:0;height:55px;display:flex;align-items:center;gap:30px;white-space:nowrap}
.footer-name{font-family:'Poppins',sans-serif;font-weight:700;font-size:13.5px}
.footer-link{display:flex;align-items:center;font-family:'Poppins',sans-serif;font-size:13px}
.footer-link svg{width:12px;height:12px;margin-right:10px;flex:none}
.footer-code{position:absolute;left:882px;top:22px;font-size:10px}
</style>
</head>
<body>
<div class="page">

  <svg class="hero-art" width="927" height="440" viewBox="0 0 927 440">
    <circle cx="735" cy="205" r="270" fill="var(--orange)"/>
    <defs>
      <linearGradient id="meetingTone" x1="0" y1="0" x2="1" y2="1">
        <stop offset="0" stop-color="#7f8f95"/>
        <stop offset="0.5" stop-color="#3f4c52"/>
        <stop offset="1" stop-color="#5c6f63"/>
      </linearGradient>
      <linearGradient id="coinTone" x1="0" y1="0" x2="1" y2="1">
        <stop offset="0" stop-color="#8c8e92"/>
        <stop offset="1" stop-color="#b88a4a"/>
      </linearGradient>
    </defs>
    <circle cx="738" cy="195" r="235" fill="url(#meetingTone)" role="img" aria-label="Photo of two businessmen in a meeting in front of a bar chart screen"/>
    <circle cx="516" cy="286" r="121" fill="var(--white)"/>
    <circle cx="516" cy="286" r="114" fill="url(#coinTone)" role="img" aria-label="Photo of hands counting cash beside stacks of coins"/>
  </svg>

  <h1 class="section-title snapshot-title">FUND SNAPSHOT</h1>
  <div class="rule" style="left:58px;top:77px;width:204px"></div>

  <div class="snapshot">
    <div class="snap-row"><span class="snap-label">Size</span><span class="snap-colon">:</span><span class="snap-value">$100M</span></div>
    <div class="snap-row"><span class="snap-label">Stage</span><span class="snap-colon">:</span><span class="snap-value">Pre-seed to Series B (focus on Seed/A)</span></div>
    <div class="snap-row"><span class="snap-label">Term</span><span class="snap-colon">:</span><span class="snap-value">10+1+1 yrs</span></div>
    <div class="snap-row"><span class="snap-label">Returns</span><span class="snap-colon">:</span><span class="snap-value">3x MOIC</span></div>
    <div class="snap-row"><span class="snap-label">IRR</span><span class="snap-colon">:</span><span class="snap-value">15–25%</span></div>
    <div class="snap-row"><span class="snap-label">Portfolio</span><span class="snap-colon">:</span><span class="snap-value">~30 startups</span></div>
    <div class="snap-row tall"><span class="snap-label">Check Size</span><span class="snap-colon">:</span><span class="snap-value" style="width:140px">$0.25M–$5M | 50% follow-on reserve</span></div>
    <div class="snap-row tall"><span class="snap-label">Regions</span><span class="snap-colon">:</span><span class="snap-value" style="width:150px">North America, Asia, Europe</span></div>
    <div class="snap-row"><span class="snap-label">Fee</span><span class="snap-colon">:</span><span class="snap-value">2.5% (declining)</span></div>
    <div class="snap-row"><span class="snap-label">Carry</span><span class="snap-colon">:</span><span class="snap-value">20%</span></div>
  </div>

  <section class="thesis-band"></section>
  <h2 class="section-title thesis-title">THESIS &amp; FOCUS</h2>
  <div class="rule" style="left:58px;top:492px;width:202px"></div>
  <p class="thesis-text">We invest in breakthrough decarbonization startups to generate venture returns and strategic value for corporate LPs. Focus areas include:</p>
  <p class="impact">Impact Goal: ≥2 Gt CO<sub style="font-size:9px">2</sub>e reduced by 2050</p>

  <ul class="focus-list">
    <li><svg viewBox="0 0 16 16"><circle cx="8" cy="8" r="8" fill="#fff"/><path d="M4.5 8.2l2.3 2.3 4.7-4.8" stroke="var(--navy-deep)" stroke-width="2" fill="none"/></svg>AI &amp; Robotics for Efficiency</li>
    <li><svg viewBox="0 0 16 16"><circle cx="8" cy="8" r="8" fill="#fff"/><path d="M4.5 8.2l2.3 2.3 4.7-4.8" stroke="var(--navy-deep)" stroke-width="2" fill="none"/></svg>Data Center Decarbonization</li>
    <li><svg viewBox="0 0 16 16"><circle cx="8" cy="8" r="8" fill="#fff"/><path d="M4.5 8.2l2.3 2.3 4.7-4.8" stroke="var(--navy-deep)" stroke-width="2" fill="none"/></svg>Clean Energy Infrastructure</li>
    <li><svg viewBox="0 0 16 16"><circle cx="8" cy="8" r="8" fill="#fff"/><path d="M4.5 8.2l2.3 2.3 4.7-4.8" stroke="var(--navy-deep)" stroke-width="2" fill="none"/></svg>Synthetic Biology &amp; Advanced Materials</li>
    <li><svg viewBox="0 0 16 16"><circle cx="8" cy="8" r="8" fill="#fff"/><path d="M4.5 8.2l2.3 2.3 4.7-4.8" stroke="var(--navy-deep)" stroke-width="2" fill="none"/></svg>Sustainable Fuels &amp; Electrification</li>
    <li><svg viewBox="0 0 16 16"><circle cx="8" cy="8" r="8" fill="#fff"/><path d="M4.5 8.2l2.3 2.3 4.7-4.8" stroke="var(--navy-deep)" stroke-width="2" fill="none"/></svg>Climate Adaptation Technologies</li>
  </ul>

  <h2 class="block-title" style="left:56px;top:688px">STRATEGIC LP PLATFORM</h2>
  <div class="rule" style="left:58px;top:719px;width:202px"></div>

  <div class="item" style="top:733px">
    <div class="item-head"><svg viewBox="0 0 16 16"><circle cx="8" cy="8" r="8" fill="var(--orange)"/><path d="M4.5 8.2l2.3 2.3 4.7-4.8" stroke="#fff" stroke-width="2" fill="none"/></svg>Collaboration</div>
    <p class="item-desc">Weekly deal reviews, co-investments, diligence insights</p>
  </div>
  <div class="item" style="top:784px">
    <div class="item-head"><svg viewBox="0 0 16 16"><circle cx="8" cy="8" r="8" fill="var(--orange)"/><path d="M4.5 8.2l2.3 2.3 4.7-4.8" stroke="#fff" stroke-width="2" fill="none"/></svg>Intelligence</div>
    <p class="item-desc">10+ research theses/year, thematic workshops, private briefings</p>
  </div>
  <div class="item" style="top:835px">
    <div class="item-head"><svg viewBox="0 0 16 16"><circle cx="8" cy="8" r="8" fill="var(--orange)"/><path d="M4.5 8.2l2.3 2.3 4.7-4.8" stroke="#fff" stroke-width="2" fill="none"/></svg>Custom Sourcing</div>
    <p class="item-desc">Tailored pipelines &amp; strategic GP access for LPs</p>
  </div>

  <h2 class="block-title" style="left:56px;top:913px">FUND I HIGHLIGHTS</h2>
  <div class="rule" style="left:58px;top:946px;width:202px"></div>

  <div class="item" style="top:965px">
    <div class="item-head"><svg viewBox="0 0 16 16"><circle cx="8" cy="8" r="8" fill="var(--orange)"/><path d="M4.5 8.2l2.3 2.3 4.7-4.8" stroke="#fff" stroke-width="2" fill="none"/></svg>Pyrexal</div>
    <p class="item-desc">Kessler Tech spinout; retrofits diesel engines for green fuels</p>
  </div>
  <div class="item" style="top:1016px">
    <div class="item-head"><svg viewBox="0 0 16 16"><circle cx="8" cy="8" r="8" fill="var(--orange)"/><path d="M4.5 8.2l2.3 2.3 4.7-4.8" stroke="#fff" stroke-width="2" fill="none"/></svg>Verdalgen</div>
    <p class="item-desc">CO<sub style="font-size:8px">2</sub>-fed algae proteins at price parity</p>
  </div>
  <div class="item" style="top:1067px">
    <div class="item-head"><svg viewBox="0 0 16 16"><circle cx="8" cy="8" r="8" fill="var(--orange)"/><path d="M4.5 8.2l2.3 2.3 4.7-4.8" stroke="#fff" stroke-width="2" fill="none"/></svg>Fibrecirc</div>
    <p class="item-desc">Recycled carbon fiber for auto/<br>industrial markets</p>
  </div>

  <section class="team">
    <h2 class="team-title">TEAM</h2>
    <div class="team-rule"></div>
    <div class="member" style="top:87px"><div class="member-name">Mara Lindqvist (MP, CA):</div><div class="member-role">Climate policy leader, investor (Halden)</div></div>
    <div class="member" style="top:144px"><div class="member-name">Priya Nathaniel, PhD (Thailand):</div><div class="member-role">10+ research theses/year, thematic workshops, private briefings</div></div>
    <div class="member" style="top:200px"><div class="member-name">Owen Tasker, PhD (NY):</div><div class="member-role">Photonics founder (Eastbrook)</div></div>
    <div class="member" style="top:257px"><div class="member-name">Lena Castell, CFA (CA):</div><div class="member-role">Energy investor (Eastbrook)</div></div>
    <div class="member" style="top:314px"><div class="member-name">Ruth Amari (CA):</div><div class="member-role">M&amp;A/legal ops (Eastbrook)</div></div>
    <div class="member" style="top:370px"><div class="member-name">Felix Brannon, JD (NY):</div><div class="member-role">Legal advisor, Orrin Capital alum (Ridgeway Law)</div></div>
  </section>

  <footer class="footer">
    <div class="footer-row">
      <span class="footer-name">MARA LINDQVIST – MANAGING PARTNER</span>
      <span class="footer-link"><svg viewBox="0 0 16 12"><rect x="0" y="0" width="16" height="12" rx="1.5" fill="var(--orange)"/><path d="M1 1.5l7 5.5 7-5.5" stroke="var(--navy-deep)" stroke-width="1.5" fill="none"/></svg>mlindqvist@northvane.earth</span>
      <span class="footer-link"><svg viewBox="0 0 16 16"><circle cx="8" cy="8" r="7" fill="var(--orange)"/><path d="M1 8h14M8 1c-3 3-3 11 0 14M8 1c3 3 3 11 0 14" stroke="var(--navy-deep)" stroke-width="1.2" fill="none"/></svg>northvane.earth</span>
    </div>
    <span class="footer-code">C38</span>
  </footer>

</div>
</body>
</html>
```